New BROVANEL keyboard

We need to redesign the plastic cover of electronic keyboard. The equipment is a cooker with an agitation system. See page http://www.valtor-kitchenworks.com/catering-machinery/industrial-kitchens-equipment/tilting-bratt-pan where you can even find a video.

One of the important features of this equipment is the mixing system. We need to give more importance on the keypad and renew all buttons and general design.

Note: On the manual instruction you can find the keypad description. The keys 13, 14 and 15 can be moved. The rest (1-12) must remain on same postion.

Reason: Uploaded dimensions (mm 95x150) and logo

```html
<!DOCTYPE html>
<html lang="en">
<head>
<meta charset="utf-8">
<title>Cooker keypad</title>
<link rel="stylesheet" href="https://fonts.googleapis.com/css2?family=Arimo:wght@400;700&family=Orbitron:wght@700&display=swap">
<style>
  :root {
    --canvas: #ffffff;
    --panel-dark: #050505;
    --panel-light: #4a4a4a;
    --key-top: #3a3a3a;
    --key-bottom: #000000;
    --ice: #9ccbe3;
    --ice-deep: #7fb6d4;
    --frame: #d2d2d2;
    --reset-red: #b3151c;
    --alert: #c8134a;
    --alert-light: #f4f4f4;
  }
  * { box-sizing: border-box; margin: 0; padding: 0; }
  html, body { width: 766px; height: 1200px; overflow: hidden; background: var(--canvas); }
  body { position: relative; font-family: "Arimo", Arial, sans-serif; }

  .keypad {
    position: absolute; left: 6px; top: 6px; width: 756px; height: 1180px;
    border-radius: 34px;
    background: linear-gradient(90deg, var(--panel-dark) 0%, #111 55%, var(--panel-light) 100%);
    box-shadow: 0 6px 0 #cfcfcf, 0 8px 6px rgba(0,0,0,.25);
  }
  .key {
    position: absolute; border-radius: 24px;
    background: linear-gradient(160deg, var(--key-top) 0%, #141414 45%, var(--key-bottom) 100%);
    box-shadow: inset 0 2px 2px rgba(255,255,255,.12), 0 3px 6px rgba(0,0,0,.6);
    display: flex; align-items: center; justify-content: center;
  }
  .key svg { display: block; }
  .label {
    position: absolute; color: var(--ice); font-size: 24px; line-height: 26px;
    text-align: center; transform: translateX(-50%); white-space: nowrap;
  }
  .readout {
    position: absolute; border: 3px solid var(--frame); border-radius: 28px;
    display: flex; align-items: center; justify-content: center;
    font-family: "Orbitron", "Arial Black", sans-serif; font-weight: 700;
    color: var(--ice); letter-spacing: -1px;
  }
  .readout sup { font-size: 0.55em; margin: 0 2px 0 4px; position: relative; top: -0.35em; }

  .reset-lines { position: absolute; left: 63px; top: 848px; width: 92px; }
  .reset-lines span { display: block; height: 4px; background: var(--reset-red); margin-bottom: 6px; }
  .reset-text {
    position: absolute; left: 198px; top: 846px; color: var(--ice);
    font-weight: 700; font-size: 33px; line-height: 36px;
  }

  .mixer-zone {
    position: absolute; left: 398px; top: 569px; width: 347px; height: 383px;
    border: 3px solid var(--frame);
  }
  .mixer-title { position: absolute; left: 426px; top: 586px; color: var(--ice); font-size: 22px; }
  .step-key { border-radius: 14px; }
</style>
</head>
<body>
  <div class="keypad"></div>

  <!-- Main power -->
  <div class="key" style="left:101px;top:67px;width:140px;height:138px;border-radius:30px;">
    <svg width="80" height="80" viewBox="0 0 80 80" aria-hidden="true">
      <path d="M25 20 A26 26 0 1 0 55 20" fill="none" stroke="var(--ice)" stroke-width="9" stroke-linecap="round"/>
      <line x1="40" y1="8" x2="40" y2="38" stroke="var(--ice)" stroke-width="9" stroke-linecap="round"/>
    </svg>
  </div>
  <div class="label" style="left:170px;top:218px;">ON/OFF</div>

  <!-- Start / pause -->
  <div class="key" style="left:523px;top:63px;width:190px;height:144px;border-radius:32px;">
    <svg width="140" height="90" viewBox="0 0 140 90" aria-hidden="true">
      <path d="M12 8 L72 45 L12 82 Z" fill="var(--ice)" stroke="var(--ice)" stroke-width="8" stroke-linejoin="round"/>
      <rect x="84" y="4" width="20" height="82" rx="7" fill="var(--ice)"/>
      <rect x="113" y="4" width="20" height="82" rx="7" fill="var(--ice)"/>
    </svg>
  </div>
  <div class="label" style="left:612px;top:218px;">START/PAUSE</div>

  <!-- Readouts -->
  <div class="readout" style="left:101px;top:283px;width:229px;height:77px;font-size:40px;">20<sup>°</sup>C</div>
  <div class="readout" style="left:98px;top:410px;width:232px;height:108px;font-size:38px;">1:00:20</div>

  <!-- Set keys -->
  <div class="key" style="left:460px;top:308px;width:86px;height:86px;">
    <svg width="66" height="66" viewBox="0 0 66 66" aria-hidden="true"><path d="M33 6 L60 58 L33 46 L6 58 Z" fill="var(--ice)" stroke="var(--ice)" stroke-width="4" stroke-linejoin="round"/></svg>
  </div>
  <div class="key" style="left:460px;top:411px;width:86px;height:86px;">
    <svg width="66" height="66" viewBox="0 0 66 66" aria-hidden="true"><path d="M33 60 L60 8 L33 20 L6 8 Z" fill="var(--ice)" stroke="var(--ice)" stroke-width="4" stroke-linejoin="round"/></svg>
  </div>
  <div class="key" style="left:606px;top:308px;width:90px;height:86px;">
    <svg width="30" height="66" viewBox="0 0 30 66" aria-hidden="true">
      <rect x="10" y="4" width="10" height="42" rx="5" fill="none" stroke="var(--ice)" stroke-width="3"/>
      <circle cx="15" cy="52" r="10" fill="var(--ice)"/>
      <rect x="13" y="22" width="4" height="28" fill="var(--ice)"/>
    </svg>
  </div>
  <div class="key" style="left:606px;top:411px;width:90px;height:86px;">
    <svg width="66" height="66" viewBox="0 0 66 66" aria-hidden="true">
      <circle cx="33" cy="33" r="25" fill="none" stroke="var(--ice)" stroke-width="6"/>
      <circle cx="33" cy="33" r="18" fill="none" stroke="var(--ice-deep)" stroke-width="1.5"/>
      <path d="M33 17 V33 H46" fill="none" stroke="var(--ice)" stroke-width="2"/>
    </svg>
  </div>

  <!-- Tilt keys -->
  <div class="key" style="left:46px;top:581px;width:109px;height:104px;">
    <svg width="90" height="70" viewBox="0 0 90 70" aria-hidden="true">
      <path d="M14 30 L80 30 L70 62 L22 62 Z" fill="none" stroke="var(--ice)" stroke-width="6" stroke-linejoin="round"/>
      <path d="M40 30 C40 14 30 10 18 10" fill="none" stroke="var(--ice)" stroke-width="5"/>
      <path d="M6 10 L20 2 L20 18 Z" fill="var(--ice)"/>
    </svg>
  </div>
  <div class="label" style="left:112px;top:698px;">ROTATE<br>BACKWARD</div>
  <div class="key" style="left:222px;top:581px;width:109px;height:104px;">
    <svg width="90" height="70" viewBox="0 0 90 70" aria-hidden="true">
      <path d="M10 30 L76 30 L68 62 L20 62 Z" fill="none" stroke="var(--ice)" stroke-width="6" stroke-linejoin="round"/>
      <path d="M50 30 C50 14 60 10 72 10" fill="none" stroke="var(--ice)" stroke-width="5"/>
      <path d="M84 10 L70 2 L70 18 Z" fill="var(--ice)"/>
    </svg>
  </div>
  <div class="label" style="left:285px;top:698px;">ROTATE<br>FORWARD</div>

  <!-- Reset -->
  <div class="reset-lines"><span></span><span></span><span></span></div>
  <div class="reset-text">RESET</div>

  <!-- Mixer -->
  <div class="mixer-zone"></div>
  <div class="mixer-title">MIXER</div>
  <div class="key" style="left:431px;top:638px;width:89px;height:84px;">
    <svg width="50" height="50" viewBox="0 0 80 80" aria-hidden="true">
      <path d="M25 20 A26 26 0 1 0 55 20" fill="none" stroke="var(--ice)" stroke-width="10" stroke-linecap="round"/>
      <line x1="40" y1="8" x2="40" y2="38" stroke="var(--ice)" stroke-width="10" stroke-linecap="round"/>
    </svg>
  </div>
  <div class="label" style="left:475px;top:738px;">ON/OFF</div>
  <div class="key" style="left:598px;top:638px;width:90px;height:84px;">
    <svg width="52" height="52" viewBox="0 0 52 52" aria-hidden="true">
      <path d="M18 10 A18 18 0 1 0 34 10" fill="none" stroke="var(--ice)" stroke-width="8"/>
      <path d="M26 2 L42 8 L30 20 Z" fill="var(--ice)"/>
    </svg>
  </div>
  <div class="label" style="left:641px;top:738px;">DIRECTION</div>

  <div class="key step-key" style="left:428px;top:822px;width:57px;height:57px;">
    <svg width="30" height="30" viewBox="0 0 30 30" aria-hidden="true"><rect x="2" y="11" width="26" height="8" rx="2" fill="var(--ice)"/></svg>
  </div>
  <div class="readout" style="left:498px;top:803px;width:150px;height:88px;font-size:46px;">20</div>
  <div class="key step-key" style="left:658px;top:822px;width:57px;height:57px;">
    <svg width="30" height="30" viewBox="0 0 30 30" aria-hidden="true"><path d="M11 2h8v9h9v8h-9v9h-8v-9H2v-8h9z" fill="var(--ice)"/></svg>
  </div>
  <div class="label" style="left:572px;top:908px;">SPEED</div>

  <!-- Emergency -->
  <div class="key" style="left:274px;top:983px;width:221px;height:202px;border-radius:44px;">
    <svg width="190" height="170" viewBox="0 0 190 170" aria-hidden="true">
      <path d="M95 10 L182 158 L8 158 Z" fill="var(--alert)" stroke="var(--alert)" stroke-width="14" stroke-linejoin="round"/>
      <path d="M95 42 L152 140 L38 140 Z" fill="var(--alert-light)" stroke="var(--alert-light)" stroke-width="8" stroke-linejoin="round"/>
      <rect x="88" y="72" width="14" height="40" rx="4" fill="#111"/>
      <rect x="88" y="118" width="14" height="14" rx="3" fill="#111"/>
    </svg>
  </div>
</body>
</html>
```